Court Heritage Trust Business Card

We need a business card design for the Court Heritage Trust. It is a non-profit organization that promotes environmental awareness and activism within the tennis community. It will include our newly designed logo. It needs to be modern yet with an elegant business feel. The market we deal with is upscale with discerning taste. Must convey a sense of seriousness that people can trust, while inspiring their highest values to create a better world.
Target Market(s)
Upscale market of tennis, business, and environmental enthusiasts
Industry/Entity Type
Non-Profit
Requirements
Must have
- Must have an elegant look, be easy to read and convey seriousness of purpose.
Show where you will place the name, title, address, email and phone number on front of the card.
Note: We have included both versions of our new logo. Feel free to use either or both. We are not sure which will be ideal for a business card. The files are in jpg. We can supply other formats if they will be easier to work with.
Nice to have
- The back side should have the following:
Printed by "PLIX" on:
100% recycled post consumer waste
100% recyclable and biodegradable
Sustainable source, Elemental Chlorine Free (ECF)
Manufactured using wind power
Include the plix logo from the images section.

```html
<!DOCTYPE html>
<html lang="en">
<head>
<meta charset="utf-8">
<title>Court Heritage Trust Business Card</title>
<link rel="stylesheet" href="https://fonts.googleapis.com/css2?family=Arimo:ital,wght@0,400;1,400&display=swap">
<style>
  :root {
    --teal: #0d6386;
    --teal-deep: #0a5574;
    --teal-emboss: #0b4f6c;
    --paper: #f7f6f2;
    --backdrop: #e4e4e2;
    --leaf: #7fb241;
    --note: #dfeef3;
  }
  * { margin: 0; padding: 0; box-sizing: border-box; }
  html, body {
    width: 1200px; height: 1200px; overflow: hidden;
    background: var(--backdrop);
    font-family: "Arimo", Arial, sans-serif;
  }
  .canvas { position: relative; width: 1200px; height: 1200px; }

  .card {
    position: absolute; left: 220px;
    width: 760px; height: 440px;
    box-shadow: 0 6px 18px rgba(0,0,0,0.12);
  }

  /* Back side */
  .card-back { top: 95px; background: var(--paper); padding: 14px; }
  .card-back .panel {
    position: relative; width: 100%; height: 100%;
    background: var(--teal);
  }
  .card-back .mark {
    position: absolute; left: 50%; top: 44px; transform: translateX(-50%);
    width: 78px; height: 78px; border-radius: 50%;
    border: 4px solid var(--teal-emboss);
  }
  .card-back .rule {
    position: absolute; left: 0; right: 0; height: 2px;
    background: var(--teal-emboss);
  }
  .card-back .rule-top { top: 140px; }
  .card-back .rule-bottom { top: 218px; }
  .card-back .org-name {
    position: absolute; left: 0; right: 0; top: 158px;
    text-align: center; font-size: 42px; letter-spacing: 1px;
    color: var(--teal-emboss); text-transform: uppercase;
  }
  .printer {
    position: absolute; left: 18px; bottom: 18px;
    display: flex; align-items: flex-end; gap: 14px;
  }
  .printer-brand { display: flex; align-items: center; gap: 6px; }
  .printer-brand .dot {
    width: 26px; height: 26px; border-radius: 50%; background: var(--leaf);
  }
  .printer-brand .label { font-size: 18px; color: var(--leaf); }
  .printer-notes {
    font-style: italic; font-size: 12px; line-height: 1.35;
    color: var(--note); list-style: none;
  }

  /* Front side */
  .card-front { top: 585px; background: var(--teal); padding: 30px; }
  .card-front .panel {
    position: relative; width: 100%; height: 100%;
    background: var(--paper);
  }
  .card-front .mark {
    position: absolute; left: 50%; top: 22px; transform: translateX(-50%);
    width: 80px; height: 80px; border-radius: 50%;
    border: 5px solid var(--teal);
  }
  .card-front .rule {
    position: absolute; left: 0; right: 0; height: 2px; background: var(--teal);
  }
  .card-front .rule-top { top: 118px; }
  .card-front .rule-bottom { top: 190px; }
  .card-front .org-name {
    position: absolute; left: 0; right: 0; top: 134px;
    text-align: center; font-size: 40px; letter-spacing: 1px;
    color: var(--teal); text-transform: uppercase;
  }
  .contact {
    position: absolute; left: 0; right: 0; top: 212px;
    text-align: center; font-size: 25px; line-height: 1.3;
    color: var(--teal-deep); font-style: normal;
  }
</style>
</head>
<body>
<main class="canvas">

  <section class="card card-back" aria-label="Card back">
    <div class="panel">
      <div class="mark" aria-hidden="true"></div>
      <div class="rule rule-top"></div>
      <h2 class="org-name">Court Heritage Trust</h2>
      <div class="rule rule-bottom"></div>
      <div class="printer">
        <div class="printer-brand">
          <span class="dot" aria-hidden="true"></span>
          <span class="label">plix</span>
        </div>
        <ul class="printer-notes">
          <li>Printed by "PLIX" on:</li>
          <li>100% recycled post consumer waste</li>
          <li>100% recyclable and biodegradable</li>
          <li>Sustainable source, Elemental Chlorine Free (ECF)</li>
          <li>Manufactured using wind power</li>
        </ul>
      </div>
    </div>
  </section>

  <section class="card card-front" aria-label="Card front">
    <div class="panel">
      <div class="mark" aria-hidden="true"></div>
      <div class="rule rule-top"></div>
      <h1 class="org-name">Court Heritage Trust</h1>
      <div class="rule rule-bottom"></div>
      <address class="contact">
        Name Surname, Position<br>
        Telephone<br>
        Email@yourname.com<br>
        www.webaddress.com
      </address>
    </div>
  </section>

</main>
</body>
</html>
```